Wordpress Design For Financial Investment Company

//** NEW WIREFRAME ADDED TO HELP WITH LAYOUT ISSUES. PLEASE REFER TO WIREFRAME IN ATTACHED FILES. NO DESIGN WILL BE CONSIDERED IF IT DOES NOT FOLLOW THE WIREFRAME. **//
//** PLEASE READ THE ENTIRE BRIEF INCLUDING ALL UPDATES TO THE BRIEF. THE CLIENT IS VERY SPECIFIC ABOUT WHAT THEY WANT AND I'VE COVERED SEVERAL THINGS IN THE UPDATES. THERE IS ALSO A VIDEO UPDATE THAT HAS SOME VALUABLE INFORMATION IN IT FOR THIS CONTEST. **//
The client is an investment advisor who needs a new website designed. The current site is http://www.velmorfield.net.
The client wants the site to be green to match the attached logo.
The home page should have relevant images in the rotator. No people hugging! This is a financial investment site, not a family counseling site.
Also, the client wants 4 buttons on the home page to highlight the 4 main areas they focus on:
Investment Advice and Education
General Financial Planning
Retirement Planning
401K Planning
The top right area of the site needs to have their phone number, a call to action, and 2 buttons.
Their phone number is 303-418-7639
The call to action should say something like "Call for a free consultation!"
The buttons need to say:
Login To Your Bluvexa Account
Login To Your Quillbrook Account
The final design should communicate professionalism, financial safety and growth.
Main navigation should be:
Home
About Us
Associates
Services
Contact
Mission Statement (Could also be "Our Mission")
This is a site that the client likes: http://www.pwkinvestmentconsulting.com/
Updates
The designs should not have:
Newsletter content. A newsletter sign up is fine
Learning Center
Calculators
Stock prices/tickers
The design should have a contact form on the page.
I have talked to my client and have some updates. I did a video update because I thought it would be easier to show what I'm trying to get across.
Reason: I am going to be extending the contest a few more days. I'm still not getting quite what I want and very few people are even trying to follow the creative brief and the updates to it.
PLEASE read the entire brief and the updates. There is also a video I made that explains everything. I've also attached a wireframe.
Thanks!
Target Market(s)
People looking for a high-end financial investment company.
Industry/Entity Type
Investment
Requirements
Must have
- !!FOLLOW THE WIREFRAME FOR LAYOUT!!
!!THEIR LOGO!!
4 buttons to highlight their main practice areas
Phone number in the top right
"Free Consultation" call to action
2 Login buttons in the top right
A contact form on the page.
Should not have
- The designs should not have:
Learning Center
Calculators
Stock prices/tickers

```html
<!DOCTYPE html>
<html lang="en">
<head>
<meta charset="utf-8">
<title>Corvane Financial, Inc.</title>
<link rel="stylesheet" href="https://fonts.googleapis.com/css2?family=Libre+Baskerville:ital,wght@1,700&family=Open+Sans:wght@400;600&family=PT+Sans+Narrow:wght@400;700&family=Yanone+Kaffeesatz:wght@400;600&display=swap">
<style>
:root{
  --teal:#2d6e64;
  --teal-dark:#23584f;
  --teal-light:#7fc7bd;
  --green-text:#1f6a4a;
  --orange:#d9541a;
  --grey-bg:#e9e9e9;
  --body-text:#5a5a5a;
  --white:#ffffff;
  --gold:#d6a21a;
  --brand-ink:#3a2a20;
}
*{box-sizing:border-box;margin:0;padding:0}
html,body{width:775px;height:1200px;overflow:hidden}
body{position:relative;background:var(--grey-bg);font-family:"Open Sans",sans-serif;color:var(--body-text)}
.abs{position:absolute}
.header{left:0;top:0;width:775px;height:140px;background:linear-gradient(180deg,#8fb8dc 0%,#c9dcec 45%,#e9e9e9 100%)}
.brand{left:40px;top:38px;width:130px;font-family:"PT Sans Narrow",sans-serif;font-weight:700;font-size:21px;line-height:24px;color:var(--brand-ink)}
.motto{left:168px;top:50px;width:290px;font-family:"Libre Baskerville",serif;font-style:italic;font-weight:700;font-size:13.5px;line-height:20px;color:#111;white-space:nowrap}
.motto .l2{display:block;padding-left:58px}
.login{top:4px;height:26px;background:var(--teal);border:1px solid #1b4a42;border-radius:3px;color:var(--white);font-size:11.5px;line-height:24px;text-align:center;box-shadow:0 1px 2px rgba(0,0,0,.3)}
.cta{left:447px;top:114px;font-family:"Yanone Kaffeesatz",sans-serif;font-weight:600;font-size:14px;color:var(--teal-dark)}
.phone{left:560px;top:100px;width:178px;text-align:right;font-family:"Yanone Kaffeesatz",sans-serif;font-weight:600;font-size:31px;line-height:34px;color:var(--teal-dark)}
.nav{left:35px;top:140px;width:705px;height:31px;background:linear-gradient(180deg,#3b8a7d,#255e55);border-radius:5px 5px 0 0;display:flex;list-style:none}
.nav li{font-family:"Yanone Kaffeesatz",sans-serif;font-size:15.5px;color:var(--white);line-height:31px;text-align:center;border-right:1px solid #4f9a8e}
.nav li:last-child{border:none}
.slider{left:35px;top:173px;width:705px;height:275px;border:2px solid var(--teal);background:linear-gradient(180deg,#c8ccc8 0%,#9aa79a 35%,#6e8a4a 60%,#5c7a38 100%)}
.slide-text{left:400px;top:200px;width:330px;font-family:"PT Sans Narrow",sans-serif;font-size:27px;line-height:33px;color:#111}
.slide-text b{font-size:36px;font-weight:700}
.credit{left:520px;top:431px;width:214px;text-align:right;font-size:7.5px;color:var(--white);white-space:nowrap}
.dots{left:352px;top:426px;width:68px;height:20px;background:var(--teal);display:flex;gap:3px;padding:5px 7px}
.dots span{width:10px;height:10px;background:#ddd;font-size:7px;line-height:10px;text-align:center;color:#333}
.dots span:first-child{background:var(--white)}
h1.welcome{left:48px;top:463px;font-weight:400;font-size:19px;color:var(--green-text)}
.intro{left:48px;top:497px;width:492px;font-size:9.1px;line-height:15px;letter-spacing:.15px;color:var(--body-text)}
.tile{width:235px;height:150px;border:1px solid #444}
.tile .pic{height:111px}
.tile .label{height:38px;background:linear-gradient(180deg,#2f7c70,#6ec2b6);color:var(--white);font-family:"Yanone Kaffeesatz",sans-serif;font-size:17px;line-height:38px;padding-left:20px;display:flex;align-items:center;gap:10px}
.form{left:559px;top:460px;width:177px;height:553px;background:#dedede;border:1px solid #c8c8c8;border-radius:6px;padding:6px 11px}
.form h2{font-family:"Open Sans",sans-serif;font-weight:600;font-size:15.5px;color:var(--green-text);text-align:center;border-bottom:2px dotted var(--teal-light);padding-bottom:1px}
.form h3{font-size:10.5px;font-weight:600;color:var(--orange);margin:4px 0 5px;line-height:13px}
.field{height:18px;background:var(--white);border:1px solid #ccc;border-radius:3px;font-size:8.5px;color:#333;padding:3px 7px;margin-bottom:5px}
.field.tall{height:42px}
.checks{display:grid;grid-template-columns:1fr 1fr;font-size:8.5px;color:#333;row-gap:3px;margin-bottom:6px}
.checks span::before{content:"";display:inline-block;width:8px;height:8px;border:1px solid #888;background:var(--white);margin-right:5px;vertical-align:-1px}
.captcha{height:17px;margin-top:8px;background:linear-gradient(90deg,#a6a6a6,#e05070 50%,#c0c0c0);font-size:9px;font-weight:600;color:#333;display:flex;justify-content:space-around;align-items:center}
.send{margin:6px auto 0;width:104px;height:24px;border-radius:4px;background:linear-gradient(180deg,#f3cd4a,var(--gold));color:var(--white);font-size:12px;line-height:24px;text-align:center}
.footer{left:0;top:1024px;width:775px;height:148px;background:var(--teal)}
.footer-top{left:0;top:1024px;width:775px;height:25px;background:#3b8174}
.footer-head{top:1027px;font-weight:400;font-size:15px;color:var(--white)}
.footer-list{font-size:11px;line-height:14.5px;color:var(--white);list-style:none}
.seal{left:544px;top:1053px;width:56px;height:92px;background:var(--white);border-radius:3px}
.copy{left:0;top:1172px;width:775px;height:28px;background:var(--teal-dark);color:#c9e1dc;font-size:7px;text-align:center;line-height:30px}
</style>
</head>
<body>
<header class="abs header"></header>
<div class="abs brand">Corvane Financial, Inc.</div>
<p class="abs motto">“Always do right. This will gratifysome<span class="l2">people &amp; astonish the rest.”</span></p>
<div class="abs login" style="left:366px;width:183px">Login To Your Quillbrook Account</div>
<div class="abs login" style="left:556px;width:182px">Login To Your Bluvexa Account</div>
<div class="abs cta">Call for a free consultation!</div>
<div class="abs phone">(303)-418-7639</div>

<ul class="abs nav">
  <li style="width:62px">HOME</li><li style="width:92px">ABOUT US</li><li style="width:97px">ASSOCIATES</li><li style="width:85px">SERVICES</li><li style="width:146px">MISSION STATEMENT</li><li style="width:107px">OUR MISSION</li><li style="width:116px">CONTACT US</li>
</ul>

<div class="abs slider" role="img" aria-label="Photo of an older couple hiking a grassy coastal hillside"></div>
<svg class="abs" style="left:42px;top:278px" width="24" height="40" viewBox="0 0 24 40"><polyline points="20,2 4,20 20,38" fill="none" stroke="#e8651e" stroke-width="3"/></svg>
<svg class="abs" style="left:709px;top:278px" width="24" height="40" viewBox="0 0 24 40"><polyline points="4,2 20,20 4,38" fill="none" stroke="#e8651e" stroke-width="3"/></svg>
<p class="abs slide-text">Only <b>42%</b> of Americans know how much money to save for retirement.</p>
<div class="abs dots"><span>1</span><span>2</span><span>3</span><span>4</span></div>
<div class="abs credit">©2012 Savings Outlook Study, Hollis Institute</div>

<h1 class="abs welcome">Welcome to Corvane Financial, Inc.</h1>
<p class="abs intro">Please remember that past performance may not be indicative of future results. Different types of investments involve varying degrees of risk, and there can be no assurance that the future performance of any specific investment, investment strategy, or product made reference to directly or indirectly in any newsletter (article) or television appearance, will be profitable, equal any corresponding indicated historical performance level(s), or be suitable for your portfolio. Due to various factors, including changing market conditions, the content may no longer be reflective of current opinions or positions. Moreover, you should not assume that any discussion or information contained in any newsletter (article) or television appearance serves as the receipt of, or as a substitute for, personalized investment advice from Corvane Financial, Inc. To the extent that a reader has any questions regarding the applicability of any specific issue discussed above to his/her individual situation, he/she is encouraged to consult with the professional advisor of his/her choosing. A copy of our current written disclosure statement discussing our advisory services and fees is available for review upon request.</p>

<div class="abs tile" style="left:48px;top:682px"><div class="pic" role="img" aria-label="Illustration of a pink piggy bank beside a chalkboard" style="background:linear-gradient(90deg,#e8ece8,#f3d6e4)"></div><div class="label"><svg width="10" height="14"><polyline points="2,1 8,7 2,13" fill="none" stroke="#fff" stroke-width="3"/></svg>Investment Advice and Education</div></div>
<div class="abs tile" style="left:305px;top:682px"><div class="pic" role="img" aria-label="Photo of hands reviewing financial charts on a desk" style="background:linear-gradient(90deg,#f2f2f2,#d89a4a)"></div><div class="label"><svg width="10" height="14"><polyline points="2,1 8,7 2,13" fill="none" stroke="#fff" stroke-width="3"/></svg>General Financial Planning</div></div>
<div class="abs tile" style="left:48px;top:854px"><div class="pic" role="img" aria-label="Photo of a piggy bank before a chalkboard reading retirement" style="background:linear-gradient(90deg,#3a3a40,#24242a)"></div><div class="label"><svg width="10" height="14"><polyline points="2,1 8,7 2,13" fill="none" stroke="#fff" stroke-width="3"/></svg>Retirement Planning</div></div>
<div class="abs tile" style="left:305px;top:854px"><div class="pic" role="img" aria-label="Photo of stones engraved with retirement account names" style="background:linear-gradient(90deg,#4a4640,#8a8478,#3a3630)"></div><div class="label"><svg width="10" height="14"><polyline points="2,1 8,7 2,13" fill="none" stroke="#fff" stroke-width="3"/></svg>401K Planning</div></div>

<form class="abs form">
  <h2>Contact Form</h2>
  <h3>How can we help you?</h3>
  <div class="field">Enter your Subject</div>
  <div class="field tall">Enter your Questions or Comments:</div>
  <h3>Contact Information</h3>
  <div class="field">Enter your name</div>
  <div class="field">Enter your Address 1</div>
  <div class="field">Enter your Address 2</div>
  <div class="field">Enter your City</div>
  <div class="field">Select one</div>
  <div class="field">Enter your Zip</div>
  <div class="field">Enter your Telephone no.</div>
  <div class="field">Enter your Fax no.</div>
  <div class="field">Enter your E-mail ID</div>
  <h3>What is the best time to contact you?</h3>
  <div class="checks"><span>Morning</span><span>Weekday</span><span>Afternoon</span><span>Weekend</span><span>Evening</span></div>
  <h3>Enter Text In Picture Below. Do not include spaces</h3>
  <div class="field"></div>
  <div class="captcha"><span>K</span><span>r</span><span>T</span><span>7</span></div>
  <div class="send">Send</div>
</form>

<footer class="abs footer"></footer>
<div class="abs footer-top"></div>
<h4 class="abs footer-head" style="left:48px">Sitemap</h4>
<h4 class="abs footer-head" style="left:265px">Contact info</h4>
<h4 class="abs footer-head" style="left:544px">Trust Report</h4>
<ul class="abs footer-list" style="left:49px;top:1055px"><li>Home</li><li>About Us</li><li>Associates</li><li>Services</li><li>Contact</li><li>Mission Statement</li><li>Our Mission</li></ul>
<div class="abs footer-list" style="left:265px;top:1053px;width:230px">2240 Aldermont Parkway #410<br>Brookvale, CO 80192<br><br>Phone: 303-418-7639 800-617-2294<br>Fax: 303-552-8106<br><br>Email: Dana@corvanefinancial.ws</div>
<div class="abs seal"></div>
<div class="abs footer-list" style="left:609px;top:1055px;width:130px">Click Here for our<br>Accreditation<br>Review and Trust Report</div>
<div class="abs copy">Copyright © 2013 Corvane Financial, Inc.  All right reserved</div>
</body>
</html>
```